Product Design for BelNova

Design Brief for BelNova Product Packaging

Objective:
Create a cohesive, elegant, and brand-consistent packaging design for the BelNova product line. The signature visual theme should reflect luxury, femininity, and clean beauty values.

---

🎨 Core Design Direction

Unified Aesthetic: All containers must prominently feature the floral pattern shown in "Pattern Reference: Image 3". This design serves as the brand's signature aesthetic and must be applied uniformly across all SKUs.

Brand Logo Placement: The BelNova logo (provided) should be clearly visible and harmoniously integrated into the patterned background.

Color Palette: Base colors should complement the brand’s primary palette: black, blush pink, and white.

---

🧴 Product-Specific Packaging Specifications

1. Mascara

Bottle Type: Sleek mascara tube with a wand applicator

Capacity: 5ml

Design: Use floral pattern from Pattern Reference Image 3. Ensure the pattern does not obstruct the readability of the logo or any regulatory text.

2. Eyebrow Growth Serum

Bottle Type: 5ml tube with fine-tip brush applicator

Capacity: 5ml

Design: Same floral pattern, scaled and applied proportionally to match the mascara for consistency

3. Eyelash Growth Serum

Bottle Type: 5ml tube with fine-tip brush (similar to the eyebrow serum, unless otherwise advised)

Capacity: 5ml

Design: Identical styling to maintain unity across lash & brow products

4. Anti-Aging Serum or Lotion

Bottle Type: 30ml airless pump bottle (preferred for hygiene and product stability)

Capacity: 30ml

Design: Apply floral pattern from Pattern Reference and scale appropriately for larger surface area

5. Hair Growth Spray

Bottle Type: 50ml fine mist spray bottle

Capacity: 50ml

Design: Pattern applied and scaled for taller profile; maintain visual harmony with skincare line

---

📦 Additional Notes

Please ensure packaging aligns with clean beauty standards (no overly glossy plastic finishes, avoid excessive secondary packaging unless sustainable).

Materials should be eco-conscious where possible.

If embossing, foil stamping, or UV finishing is available for logo accents, please suggest options.

```html
<!DOCTYPE html>
<html lang="en">
<head>
<meta charset="UTF-8">
<title>BelNova Hair Growth Spray – Box and Bottle Labels</title>
<link rel="stylesheet" href="https://fonts.googleapis.com/css2?family=Playfair+Display:wght@400&family=Urbanist:wght@600&display=swap">
<style>
  :root {
    --backdrop: #f5f5f5;
    --panel-white: #fdfbfb;
    --blush: #f4cfc6;
    --blush-soft: #fae6e1;
    --pattern-tone: #f1c2b8;
    --ink: #141414;
    --cap-black: #262626;
    --gold-dark: #b8860b;
    --gold-light: #fbef7a;
  }
  * { margin: 0; padding: 0; box-sizing: border-box; }
  html, body {
    width: 1039px;
    height: 1200px;
    overflow: hidden;
    background: var(--backdrop);
  }
  .canvas {
    position: relative;
    width: 1039px;
    height: 1200px;
  }

  /* shared pieces */
  .floral-band {
    position: absolute;
    left: 0;
    top: 0;
    width: 100%;
    background:
      radial-gradient(circle at 28% 22%, var(--pattern-tone) 0, transparent 30%),
      radial-gradient(circle at 75% 40%, var(--pattern-tone) 0, transparent 28%),
      radial-gradient(circle at 40% 78%, var(--pattern-tone) 0, transparent 30%),
      radial-gradient(circle at 88% 85%, var(--blush) 0, transparent 25%),
      linear-gradient(160deg, #fff 0%, var(--blush-soft) 50%, #fff 100%);
  }
  .gold-rule {
    position: absolute;
    left: 0;
    width: 100%;
    background: linear-gradient(90deg, var(--gold-dark) 0%, var(--gold-light) 30%, #d9b43a 55%, var(--gold-light) 80%, var(--gold-dark) 100%);
  }
  .label-field {
    position: absolute;
    left: 0;
    width: 100%;
    bottom: 0;
    background:
      radial-gradient(ellipse at 0% 15%, var(--blush-soft) 0, transparent 30%),
      radial-gradient(ellipse at 100% 55%, var(--blush-soft) 0, transparent 30%),
      radial-gradient(ellipse at 15% 100%, var(--blush) 0, transparent 40%),
      radial-gradient(ellipse at 90% 100%, var(--blush-soft) 0, transparent 40%),
      var(--panel-white);
  }
  .brand-name,
  .product-name,
  .volume {
    position: absolute;
    left: 0;
    width: 100%;
    text-align: center;
    color: var(--ink);
    line-height: 1;
  }
  .brand-name {
    font-family: "Playfair Display", serif;
    font-weight: 400;
  }
  .product-name,
  .volume {
    font-family: "Urbanist", sans-serif;
    font-weight: 600;
  }
  .product-name { line-height: 1.08; }

  /* carton front */
  .box-front {
    position: absolute;
    left: 107px;
    top: 105px;
    width: 416px;
    height: 990px;
    background: var(--panel-white);
    overflow: hidden;
    box-shadow: 0 6px 24px rgba(0, 0, 0, 0.08);
  }
  .box-front .floral-band { height: 399px; }
  .box-front .gold-rule { top: 399px; height: 9px; }
  .box-front .label-field { top: 408px; }
  .box-front .brand-name { top: 595px; font-size: 62px; }
  .box-front .product-name { top: 790px; font-size: 32px; }
  .box-front .volume { top: 1006px; font-size: 31px; }

  /* spray bottle */
  .spray-bottle {
    position: absolute;
    left: 615px;
    top: 107px;
    width: 319px;
    height: 986px;
  }
  .bottle-cap {
    position: absolute;
    left: 0;
    top: 0;
    width: 100%;
    height: 210px;
    background: var(--cap-black);
    border-radius: 28px 28px 0 0;
  }
  .bottle-label {
    position: absolute;
    left: 0;
    top: 210px;
    width: 100%;
    height: 776px;
    background: var(--panel-white);
    overflow: hidden;
    border-radius: 0 0 22px 22px;
    box-shadow: 0 6px 24px rgba(0, 0, 0, 0.08);
  }
  .bottle-label .floral-band { height: 276px; }
  .bottle-label .gold-rule { top: 276px; height: 7px; }
  .bottle-label .label-field { top: 283px; }
  .bottle-label .brand-name { top: 459px; font-size: 50px; }
  .bottle-label .product-name { top: 613px; font-size: 26px; }
  .bottle-label .volume { top: 796px; font-size: 25px; }
</style>
</head>
<body>
  <main class="canvas">
    <section class="box-front">
      <div class="floral-band" role="img" aria-label="Blush pink line-drawn floral pattern of peonies, lilies and leafy sprigs on white"></div>
      <div class="gold-rule"></div>
      <div class="label-field"></div>
      <h1 class="brand-name">BelNova</h1>
      <p class="product-name">Hair Growth<br>Spray</p>
      <p class="volume">50ml</p>
    </section>

    <section class="spray-bottle">
      <div class="bottle-cap"></div>
      <div class="bottle-label">
        <div class="floral-band" role="img" aria-label="Blush pink line-drawn floral pattern of peonies, lilies and leafy sprigs on white"></div>
        <div class="gold-rule"></div>
        <div class="label-field"></div>
        <h2 class="brand-name">BelNova</h2>
        <p class="product-name">Hair Growth<br>Spray</p>
        <p class="volume">50ml</p>
      </div>
    </section>
  </main>
</body>
</html>
```